Bref créative
Business cards, stationary, envelopes for investment firm
Whitford Crest Holdings
Simple
Mark L. Tressel
Principal
4618 W. Pellham Avenue, Suite 207
Marlow, OR 97142
mark@whitfordch.com
www.whitfordch.com
Please provide a design that is clean and simple. Also, we require files with editable text as well.
Please use design logo in your design

```html
<!DOCTYPE html>
<html lang="en">
<head>
<meta charset="utf-8">
<title>Whitford Crest Holdings — Business Card</title>
<link rel="stylesheet" href="https://fonts.googleapis.com/css2?family=Cinzel:wght@400;600&display=swap">
<style>
  :root {
    --navy: #34488f;
    --ink: #2f3a63;
    --grey: #6d7079;
    --paper: #ffffff;
    --backdrop: #e9e7e3;
  }
  html, body {
    margin: 0;
    padding: 0;
    width: 1200px;
    height: 900px;
    overflow: hidden;
    background: var(--backdrop);
  }
  .canvas {
    position: relative;
    width: 1200px;
    height: 900px;
  }
  .card {
    position: absolute;
    left: 100px;
    top: 164px;
    width: 1000px;
    height: 572px;
    background: var(--paper);
    overflow: hidden;
    font-family: "Cinzel", "Times New Roman", serif;
    color: var(--ink);
  }
  .card-accent {
    position: absolute;
    inset: 0;
  }
  .brand {
    position: absolute;
    left: 58px;
    top: 150px;
    display: flex;
    align-items: center;
    gap: 16px;
  }
  .brand-dot {
    width: 60px;
    height: 60px;
    border-radius: 50%;
    background: var(--navy);
    flex: none;
  }
  .brand-name {
    margin: 0;
    font-weight: 400;
    color: var(--navy);
    line-height: 1;
  }
  .brand-name .line-main {
    display: block;
    font-size: 38px;
    letter-spacing: 0.5px;
  }
  .brand-name .line-sub {
    display: block;
    margin-top: 6px;
    font-size: 20px;
    letter-spacing: 9px;
  }
  .person {
    position: absolute;
    left: 58px;
    top: 300px;
  }
  .person-name {
    margin: 0;
    font-size: 24px;
    font-weight: 400;
    color: var(--navy);
    letter-spacing: 0.5px;
  }
  .person-title {
    margin: 6px 0 0;
    font-size: 15px;
    color: var(--grey);
    letter-spacing: 1px;
  }
  .contact-list {
    list-style: none;
    margin: 24px 0 0;
    padding: 0;
    font-size: 13px;
    color: var(--grey);
    letter-spacing: 0.5px;
  }
  .contact-list li {
    display: flex;
    align-items: flex-start;
    gap: 10px;
    line-height: 20px;
  }
  .contact-list .icon {
    width: 14px;
    height: 14px;
    margin-top: 3px;
    flex: none;
  }
  .contact-list .address span { display: block; }
</style>
</head>
<body>
<div class="canvas">
  <div class="card">
    <svg class="card-accent" width="1000" height="572" viewBox="0 0 1000 572" aria-hidden="true">
      <circle cx="890" cy="170" r="310" fill="var(--navy)"/>
    </svg>

    <div class="brand">
      <div class="brand-dot" aria-hidden="true"></div>
      <p class="brand-name">
        <span class="line-main">WHITFORD CREST</span>
        <span class="line-sub">HOLDINGS</span>
      </p>
    </div>

    <div class="person">
      <h1 class="person-name">Mark L. Tressel</h1>
      <p class="person-title">Principal</p>

      <ul class="contact-list">
        <li class="address">
          <svg class="icon" viewBox="0 0 14 14" aria-hidden="true"><circle cx="7" cy="7" r="7" fill="var(--navy)"/><path d="M7 3.2a2.4 2.4 0 0 0-2.4 2.4C4.6 7.6 7 10.8 7 10.8s2.4-3.2 2.4-5.2A2.4 2.4 0 0 0 7 3.2z" fill="#fff"/><circle cx="7" cy="5.6" r="0.9" fill="var(--navy)"/></svg>
          <div><span>4618 W. Pellham Avenue, Suite 207</span><span>Marlow, OR 97142</span></div>
        </li>
        <li>
          <svg class="icon" viewBox="0 0 14 14" aria-hidden="true"><circle cx="7" cy="7" r="7" fill="var(--navy)"/><path d="M4.6 3.6l1.3-.3.8 1.9-.9.7c.4.9 1.1 1.6 2 2l.7-.9 1.9.8-.3 1.3c-3 .2-5.7-2.5-5.5-5.5z" fill="#fff"/></svg>
          <span>541-555-0147</span>
        </li>
        <li>
          <svg class="icon" viewBox="0 0 14 14" aria-hidden="true"><circle cx="7" cy="7" r="7" fill="var(--navy)"/><rect x="4" y="5.5" width="6" height="4" rx="0.6" fill="#fff"/><rect x="5" y="3.5" width="4" height="2" fill="#fff"/></svg>
          <span>541-555-0192</span>
        </li>
        <li>
          <svg class="icon" viewBox="0 0 14 14" aria-hidden="true"><circle cx="7" cy="7" r="7" fill="var(--navy)"/><rect x="5" y="3.2" width="4" height="7.6" rx="0.8" fill="#fff"/></svg>
          <span>541-555-0163</span>
        </li>
        <li>
          <svg class="icon" viewBox="0 0 14 14" aria-hidden="true"><circle cx="7" cy="7" r="7" fill="var(--navy)"/><rect x="3.6" y="4.6" width="6.8" height="4.8" rx="0.5" fill="#fff"/><path d="M3.8 4.8L7 7.3l3.2-2.5" stroke="var(--navy)" stroke-width="0.8" fill="none"/></svg>
          <span>mark@whitfordch.com</span>
        </li>
        <li>
          <svg class="icon" viewBox="0 0 14 14" aria-hidden="true"><circle cx="7" cy="7" r="7" fill="var(--navy)"/><circle cx="7" cy="7" r="3.4" stroke="#fff" stroke-width="0.9" fill="none"/><path d="M3.6 7h6.8M7 3.6c-1.6 2-1.6 4.8 0 6.8M7 3.6c1.6 2 1.6 4.8 0 6.8" stroke="#fff" stroke-width="0.7" fill="none"/></svg>
          <span>www.whitfordch.com</span>
        </li>
      </ul>
    </div>
  </div>
</div>
</body>
</html>
```